Lumora Activewear business card design

I need a business card designed for my activewear business. I would like to use the colours pink, purple white and blue. please see attached logo. please include (name) Harriet Welloby (phone) 0417582064 (email) hattieslumora@mailvento.com (ABN) 48715290637 . please include - Free shipping on all orders over $100

Target Market(s)

female

Contact Information for Business Card

Colors

Requirements
Must have
• I need a business card designed for my activewear business. I would like to use the colours pink, purple white and blue. please see attached logo. please include (name) Harriet Welloby (phone) 0417582064 (email) hattieslumora@mailvento.com (ABN) 48715290637 . please include - Free shipping on all orders over $100

```html
<!DOCTYPE html>
<html lang="en">
<head>
<meta charset="utf-8">
<title>Lumora Activewear business card</title>
<link rel="stylesheet" href="https://fonts.googleapis.com/css2?family=Roboto:wght@400;500&family=Roboto+Condensed:wght@400&display=swap">
<style>
  :root {
    --backdrop: #2a2a2c;
    --card-white: #ffffff;
    --brand-purple: #9a1bb0;
    --brand-purple-deep: #8d17a3;
    --brand-pink: #c86fb0;
    --pattern-light: #a53bba;
    --text-grey: #4a4a4a;
    --divider: #c4c4c4;
  }
  * { box-sizing: border-box; margin: 0; padding: 0; }
  html, body {
    width: 1200px; height: 801px; overflow: hidden;
    background: var(--backdrop);
    font-family: "Roboto", Arial, sans-serif;
  }
  .stage {
    position: relative; width: 1200px; height: 801px;
  }
  .card {
    position: absolute; width: 540px; height: 309px;
    border-radius: 3px;
    overflow: hidden;
  }
  .card--front {
    left: 330px; top: 68px;
    background: var(--card-white);
  }
  .card--back {
    left: 330px; top: 420px;
    background: var(--brand-purple);
  }

  /* front */
  .brand {
    position: absolute; left: 44px; top: 118px;
    display: flex; align-items: center; gap: 12px;
  }
  .brand__dot {
    width: 30px; height: 30px; border-radius: 50%;
    background: var(--brand-pink);
  }
  .brand__name {
    font-family: "Roboto", Arial, sans-serif;
    font-weight: 500; font-size: 40px; letter-spacing: 1px;
    color: var(--brand-purple);
  }
  .divider {
    position: absolute; left: 268px; top: 70px;
    width: 1px; height: 150px; background: var(--divider);
  }
  .contact {
    position: absolute; left: 292px; top: 90px;
    color: var(--text-grey); font-size: 15px;
  }
  .contact__name {
    font-weight: 500; font-size: 24px; color: var(--brand-purple);
    margin-bottom: 10px;
  }
  .contact__line {
    display: flex; align-items: center; gap: 8px;
    height: 21px;
  }
  .contact__line svg { width: 12px; height: 12px; fill: var(--brand-purple); flex: none; }
  .contact__abn { margin-top: 4px; }

  /* back */
  .pattern {
    position: absolute; inset: 0;
    background: linear-gradient(135deg, var(--brand-purple) 0%, var(--pattern-light) 50%, var(--brand-purple-deep) 100%);
    opacity: 0.55;
  }
  .offer {
    position: absolute; right: 36px; bottom: 30px;
    text-align: center; color: #fff;
    font-family: "Roboto Condensed", "Arial Narrow", sans-serif;
    font-size: 22px; line-height: 1.1;
  }
</style>
</head>
<body>
<main class="stage">
  <section class="card card--front" aria-label="Business card front">
    <div class="brand">
      <span class="brand__dot" aria-hidden="true"></span>
      <span class="brand__name">Lumora</span>
    </div>
    <div class="divider"></div>
    <div class="contact">
      <p class="contact__name">Harriet Welloby</p>
      <p class="contact__line">
        <svg viewBox="0 0 24 24" aria-hidden="true"><path d="M6.6 10.8a15 15 0 0 0 6.6 6.6l2.2-2.2a1 1 0 0 1 1-.25 11.4 11.4 0 0 0 3.6.57 1 1 0 0 1 1 1V20a1 1 0 0 1-1 1A17 17 0 0 1 3 4a1 1 0 0 1 1-1h3.5a1 1 0 0 1 1 1c0 1.25.2 2.45.57 3.57a1 1 0 0 1-.25 1z"/></svg>
        0417582064
      </p>
      <p class="contact__line">
        <svg viewBox="0 0 24 24" aria-hidden="true"><path d="M2 5h20v14H2z M2 5l10 8 10-8" /></svg>
        hattieslumora@mailvento.com
      </p>
      <p class="contact__line">
        <svg viewBox="0 0 24 24" aria-hidden="true"><circle cx="12" cy="12" r="10"/></svg>
        www.hattieslumora.com
      </p>
      <p class="contact__line contact__abn">ABN: 48715290637</p>
    </div>
  </section>

  <section class="card card--back" aria-label="Business card back">
    <div class="pattern" role="img" aria-label="Faint repeating heart outline pattern"></div>
    <p class="offer">Free shipping on all<br>orders over $100</p>
  </section>
</main>
</body>
</html>
```